Our private family owned investment company owns a vineyard in Napa. We want to design a label to put on our wine bottles once wine is ready. We would like artists to develop a creative design for a new label using this wording: Vineyard 48172. The dimensions of the label will be the standard label size on a 750 ml wine bottle. We appreciate creative flair, a classy look, preferably color but open to black and white too; maybe submit both ways. **As more explanation for designers, our family founded and owned a business for over 50 years and our logo was a teal colored snowflake (see attached jpeg logo). Our first plant address was numbered 48172. After our business was sold, our new family office is on located at 48172 Dunmore. We have created a new business logo (see attached blue TRB logo) So the 48172 and 2 logos all have lineage and sentimental value to our family. Thank you for providing your unique creativity to this project.

Target Market(s)

to inspire conversation and reminiscing among friends and business associates when entertaining them.

Industry/Entity Type

Investment

Colors

Designer to choose colors to be used in the design.

Requirements
Must have
• Must Incorporate the wording: Vineyard 48172 - as part of the entire design and please see the attached logos (sketch of Vineyard 48172, blue snowflake logo, and TRB logo) and use any of these as a base, or part of, your new design. ** See project description for more detail on the meaning behind these logos.**

```html
<!DOCTYPE html>
<html lang="en">
<head>
<meta charset="utf-8">
<title>Vineyard 48172 – Cabernet Sauvignon Label</title>
<link rel="stylesheet" href="https://fonts.googleapis.com/css2?family=Cinzel:wght@400;500&family=Arvo:wght@700&display=swap">
<style>
  :root {
    --silver-light: #f1f1f1;
    --silver-mid: #d9d9d9;
    --silver-dark: #bdbdbd;
    --label-black: #141414;
    --brand-blue: #1890d2;
    --brand-blue-deep: #0f6fa8;
    --gold-light: #efe3bf;
    --gold-dark: #a8925a;
    --ink: #1b1b1b;
  }
  * { margin: 0; padding: 0; box-sizing: border-box; }
  html, body {
    width: 801px;
    height: 1200px;
    overflow: hidden;
    background: var(--label-black);
  }
  .label {
    position: relative;
    width: 801px;
    height: 1200px;
    overflow: hidden;
  }
  .label-art {
    position: absolute;
    inset: 0;
  }
  .wordmark {
    position: absolute;
    left: 0;
    width: 100%;
    text-align: center;
    font-family: "Cinzel", serif;
    font-weight: 400;
    color: var(--ink);
    line-height: 1;
  }
  .wordmark-title {
    top: 78px;
    font-size: 108px;
    letter-spacing: 1px;
  }
  .wordmark-number {
    top: 240px;
    font-size: 96px;
    letter-spacing: 2px;
  }
  .brand-name {
    position: absolute;
    top: 470px;
    left: 0;
    width: 100%;
    text-align: center;
    font-family: "Cinzel", serif;
    font-weight: 500;
    font-size: 170px;
    line-height: 1;
    color: var(--brand-blue);
    letter-spacing: 6px;
  }
  .varietal {
    position: absolute;
    left: 0;
    width: 100%;
    text-align: center;
    font-family: "Arvo", serif;
    font-weight: 700;
    color: var(--brand-blue);
    line-height: 1;
  }
  .varietal-primary {
    top: 905px;
    font-size: 92px;
    letter-spacing: 3px;
  }
  .varietal-secondary {
    top: 1030px;
    font-size: 66px;
    letter-spacing: 2px;
  }
</style>
</head>
<body>
  <main class="label">
    <svg class="label-art" width="801" height="1200" viewBox="0 0 801 1200" aria-hidden="true">
      <defs>
        <linearGradient id="silverFace" x1="0" y1="0" x2="1" y2="0">
          <stop offset="0" stop-color="var(--silver-dark)"/>
          <stop offset="0.5" stop-color="var(--silver-light)"/>
          <stop offset="1" stop-color="var(--silver-mid)"/>
        </linearGradient>
        <linearGradient id="goldBand" x1="0" y1="0" x2="1" y2="0">
          <stop offset="0" stop-color="var(--gold-dark)"/>
          <stop offset="0.5" stop-color="var(--gold-light)"/>
          <stop offset="1" stop-color="var(--gold-dark)"/>
        </linearGradient>
      </defs>
      <!-- upper silver panel -->
      <rect class="panel-silver" x="0" y="0" width="801" height="720" fill="url(#silverFace)"/>
      <!-- chevron bands -->
      <polygon class="band-blue" points="0,640 400,800 801,640 801,656 400,816 0,656" fill="var(--brand-blue)"/>
      <polygon class="band-gold" points="0,674 400,834 801,674 801,704 400,880 0,704" fill="url(#goldBand)"/>
      <!-- lower black panel -->
      <polygon class="panel-black" points="0,704 400,880 801,704 801,1200 0,1200" fill="var(--label-black)"/>
    </svg>

    <h1 class="wordmark wordmark-title">Vineyard</h1>
    <p class="wordmark wordmark-number">48172</p>

    <p class="brand-name">TRB</p>

    <p class="varietal varietal-primary">Cabernet</p>
    <p class="varietal varietal-secondary">Sauvignon</p>
  </main>
</body>
</html>
```